依頼詳細
開設告知を病院や行政、居宅介護支援事業所に行うための簡易的なチラシの作成をお願いいたします。情報量は最低限で、雰囲気重視、まずは時期と場所をしっかりと伝えて初期段階の営業を行うためのツールを想定しています。
記載項目
別紙資料をご確認ください。
サイズ
A4
ページ数
片面
希望イメージ
シンプル 複雑
単色 カラフル
暗い 明るい
日常 高級
遊び心 厳粛
未来的 伝統的
女性的 男性的
希望する色
納品ファイル
補足説明

スタッフの投票で決めました。

大変すばらしい提案をいただきましてありがとうございました。今後もパンフレット等、様々依頼をさせていただく予定ですので、今後とも宜しくお願い致します。

```html
<!DOCTYPE html>
<html lang="ja">
<head>
<meta charset="utf-8">
<title>新規開設のお知らせ</title>
<link rel="stylesheet" href="https://fonts.googleapis.com/css2?family=Noto+Sans+JP:wght@400;500;700;900&family=Noto+Serif+JP:wght@600;700&display=swap">
<style>
:root{
  --blue:#2a6fc0;
  --blue-dark:#1c559b;
  --blue-pale:#dcebf8;
  --blue-line:#9cc4e8;
  --red:#d6332b;
  --text:#333;
  --white:#fff;
}
*{margin:0;padding:0;box-sizing:border-box}
html,body{width:848px;height:1200px;overflow:hidden;background:#fff}
body{font-family:"Noto Sans JP",sans-serif;color:var(--text)}
.flyer{position:relative;width:848px;height:1200px;overflow:hidden;
  background:linear-gradient(180deg,#fff 60%,#e6f1fb 100%)}
.hero-photo{position:absolute;left:0;top:0;width:848px;height:612px;
  background:linear-gradient(160deg,#f4f1e6 0%,#e9e4cf 22%,#c9d9a8 45%,#8fb37a 70%,#6c8f63 100%)}
.tagline{position:absolute;left:36px;top:22px;font-family:"Noto Serif JP",serif;
  font-weight:700;font-size:25px;line-height:1.45;color:#c5452c;letter-spacing:.04em}
.headline{position:absolute;left:44px;top:330px;color:var(--white);font-weight:900;
  font-size:50px;line-height:1.3;letter-spacing:.02em;
  text-shadow:0 0 8px rgba(20,60,120,.8),2px 2px 0 rgba(20,60,120,.6)}
.features{position:absolute;left:38px;top:630px;width:500px;list-style:none}
.features li{font-size:15px;line-height:1.6;padding:10px 4px 12px;border-bottom:2px solid var(--blue-line)}
.fees{position:absolute;left:562px;top:630px;width:250px;border-collapse:collapse;font-size:16px}
.fees caption{background:var(--blue);color:var(--white);font-weight:700;font-size:15px;padding:3px 0;letter-spacing:.3em}
.fees td{padding:4px 10px;font-weight:500}
.fees td.amount{text-align:right}
.fees tr.total td{border-top:2px solid var(--blue);font-weight:700;font-size:18px}
.fees-note{position:absolute;left:566px;top:780px;font-size:10px;color:#555}
.map{position:absolute;left:562px;top:800px;width:250px;height:136px;
  background:linear-gradient(135deg,#e9f1e4,#cfe3f3);border:1px solid #bbb}
.annex{position:absolute;left:38px;top:912px;display:flex;align-items:center;gap:10px}
.annex-label{font-size:22px;font-weight:900;color:var(--blue-dark)}
.annex-item{background:var(--blue);color:var(--white);font-size:20px;font-weight:700;padding:2px 12px}
.brand{position:absolute;left:38px;top:970px;width:150px;display:flex;flex-direction:column;align-items:center;gap:6px;color:var(--blue-dark)}
.brand-mark{width:44px;height:44px;border-radius:50%;background:var(--blue-dark)}
.brand-kind{font-size:10px;font-weight:700}
.brand-name{font-size:26px;font-weight:700;letter-spacing:.1em}
.contact{position:absolute;left:206px;top:960px;color:var(--blue-dark)}
.contact-lead{font-size:16px;font-weight:700;color:var(--text);margin-left:6px}
.phone{display:flex;align-items:center;gap:8px;margin-top:2px}
.phone-label{background:var(--blue-dark);color:var(--white);font-size:11px;font-weight:700;line-height:1.2;padding:4px 5px;text-align:center}
.phone-number{font-size:52px;font-weight:900;letter-spacing:.02em;line-height:1.1}
.phone svg{width:40px;height:40px}
.address{font-size:26px;font-weight:900;color:var(--text);margin-top:4px}
.access{position:absolute;left:206px;top:1120px;border:2px solid var(--red);background:var(--white);
  color:var(--red);font-size:17px;font-weight:700;padding:3px 12px}
</style>
</head>
<body>
<main class="flyer">
  <div class="hero-photo" role="img" aria-label="木漏れ日の中、車いすの高齢男性を囲んで笑顔で過ごす家族の写真"></div>
  <p class="tagline">ご利用者様とご家族の<br>笑顔あふれる暮らしを<br>サポートいたします。</p>
  <h1 class="headline">令和3年4月<br>群馬県みずほ市に<br>新しい介護施設が<br>新規開設します。</h1>

  <ul class="features">
    <li>若葉沼ふれあい公園徒歩1分。自然豊かで落ち着いたホームです。</li>
    <li>理学療法士、作業療法士を配置し、機能訓練に力を入れています。そよかぜで出来ることを増やしていきましょう。</li>
    <li>シアタールーム等、余暇設備が充実しています。</li>
    <li>畑・園芸スペースもあります。認知機能向上のために様々な植物の栽培を楽しめます。</li>
  </ul>

  <table class="fees">
    <caption>費用例</caption>
    <tr><td>家賃</td><td class="amount">27,000円〜</td></tr>
    <tr><td>食費</td><td class="amount">39,000円</td></tr>
    <tr><td>管理費</td><td class="amount">18,000円</td></tr>
    <tr class="total"><td>合計</td><td class="amount">84,000円〜</td></tr>
  </table>
  <p class="fees-note">※別途介護サービス費</p>
  <div class="map" role="img" aria-label="施設周辺の案内地図"></div>

  <div class="annex">
    <span class="annex-label">併設施設</span>
    <span class="annex-item">訪問介護事業所</span>
    <span class="annex-item">通所介護事業所</span>
  </div>

  <div class="brand">
    <span class="brand-mark"></span>
    <span class="brand-kind">住宅型有料老人ホーム</span>
    <span class="brand-name">そよかぜ</span>
  </div>

  <div class="contact">
    <p class="contact-lead">お気軽にお問い合わせください。</p>
    <div class="phone">
      <span class="phone-label">開設<br>準備室</span>
      <svg viewBox="0 0 24 24" aria-hidden="true"><path fill="#1c559b" d="M6.6 10.8a15 15 0 0 0 6.6 6.6l2.2-2.2a1 1 0 0 1 1-.25 11.4 11.4 0 0 0 3.6.57 1 1 0 0 1 1 1V20a1 1 0 0 1-1 1A17 17 0 0 1 3 4a1 1 0 0 1 1-1h3.5a1 1 0 0 1 1 1c0 1.25.2 2.45.57 3.57a1 1 0 0 1-.25 1z"/></svg>
      <span class="phone-number">0000-00-0000</span>
    </div>
    <p class="address">群馬県みずほ市若葉町1234-5</p>
  </div>
  <p class="access">「東西自動車道若葉ICから車で1分|首都圏からのアクセス良好!」</p>
</main>
</body>
</html>
```